New audiology website PSD design only - guaranteed

We need a clean and attractive website to replace an existing Audiology (hearing technology) website which will be wordpress based.
The current website is: http://pelmorahearing.com.au
They have a new logo and colors which you can find at www.quodel.net/temp/plh2018.pdf
We will no longer have a web shop in the new website
To enter the competition, we only need a sample of the home page.
The winning design will be asked to produce 2 standard page template alternatives as well (based on the winning home page design, but for a standard page layout)
The winning design must provide any photos used
We want a clean, credible site but with some warmth
Target Market(s)
All ages but needs to include the elderly
Industry/Entity Type
Medical And Science
Number of Pages Required
3 page
Look and feel
Each slider illustrates characteristics of the customer's brand and the style your logo design should communicate.

```html
<!DOCTYPE html>
<html lang="en">
<head>
<meta charset="utf-8">
<title>Pelmora Hearing – Home</title>
<link href="https://fonts.googleapis.com/css2?family=Cinzel:wght@700;900&family=Crimson+Pro:wght@600;700&family=Open+Sans:wght@400;600;700&display=swap" rel="stylesheet">
<style>
:root{
  --orange:#f26a1b;
  --orange-deep:#f05a0a;
  --orange-light:#ff9a2e;
  --pink:#ff2d8a;
  --ink:#111111;
  --grey:#6b6b6b;
  --grey-light:#8a8a8a;
  --field:#ececec;
  --white:#ffffff;
}
*{box-sizing:border-box;margin:0;padding:0}
html,body{width:1200px;height:2936px;overflow:hidden}
body{
  position:relative;
  font-family:"Open Sans",Arial,sans-serif;
  color:var(--grey);
  background:
    radial-gradient(ellipse 520px 420px at 1120px 220px, rgba(255,45,138,.55), transparent 70%),
    radial-gradient(ellipse 600px 360px at 900px 120px, rgba(255,160,60,.45), transparent 70%),
    radial-gradient(ellipse 700px 300px at 300px 1760px, rgba(255,120,150,.18), transparent 70%),
    radial-gradient(ellipse 700px 300px at 950px 1580px, rgba(255,150,80,.2), transparent 70%),
    radial-gradient(ellipse 600px 260px at 100px 1000px, rgba(255,120,150,.15), transparent 70%),
    var(--white);
}
.abs{position:absolute}

/* header */
.site-header{left:78px;top:0;width:1047px;height:102px;background:rgba(255,255,255,.92)}
.brand{left:10px;top:38px;display:flex;align-items:center;gap:10px;font-family:"Open Sans",sans-serif;font-weight:600;font-size:30px;color:#333}
.brand-dot{width:28px;height:28px;border-radius:50%;border:3px solid var(--orange)}
.main-nav{right:12px;top:68px;display:flex;gap:17px;font-size:14.5px;color:#333}
.header-tools{right:14px;top:14px;display:flex;align-items:center;gap:20px;font-size:19px;font-weight:600;color:#333}
.header-tools .divider{width:1px;height:40px;background:#bbb}
.phone-link{display:flex;align-items:center;gap:8px}

/* hero */
.hero-product{left:78px;top:137px;width:470px;height:510px;border-radius:40px;
  background:linear-gradient(160deg,#e9e9e9,#8d8d8d 55%,#3a3a3a);opacity:.9}
.hero-title{right:80px;top:222px;font-family:"Cinzel",serif;font-weight:900;font-size:80px;color:var(--ink);letter-spacing:1px;text-shadow:3px 4px 5px rgba(0,0,0,.35)}
.hero-sub{right:80px;top:318px;width:620px;text-align:right;font-weight:700;font-size:30px;line-height:1.15;color:#6a6a6a}

.btn{display:flex;align-items:center;justify-content:center;background:var(--ink);color:var(--white);
  border:3px solid var(--orange);border-radius:40px;box-shadow:0 0 0 2px var(--ink);font-size:19px;letter-spacing:.5px}
.hero-btn{left:857px;top:411px;width:264px;height:68px;font-size:25px;color:var(--orange-light)}

/* cards */
.card{border-radius:18px;overflow:hidden;background:rgba(255,255,255,.85)}
.card-aids{left:78px;top:679px;width:505px;height:658px;box-shadow:0 0 10px rgba(0,0,0,.35)}
.card-title{font-family:"Crimson Pro",serif;font-weight:700;color:var(--orange);font-size:56px;line-height:1}
.card-text{font-size:14.5px;line-height:1.45;color:var(--grey)}
.card-aids .card-title{position:absolute;left:24px;top:50px}
.card-aids .card-text{position:absolute;left:24px;top:122px;width:450px}
.card-aids .btn{position:absolute;left:22px;top:293px;width:186px;height:48px}
.aids-photo{position:absolute;left:0;top:385px;width:505px;height:230px;
  background:linear-gradient(90deg,#d8d8d8,#c9a77f 45%,#b7b7b7 70%,#e8e8e8)}

.card-services{left:616px;top:679px;width:505px;height:311px;border:1px solid #e6cccc;
  background:linear-gradient(90deg,#fff 55%,rgba(255,225,225,.9))}
.services-photo{position:absolute;right:0;top:0;width:175px;height:311px;
  background:linear-gradient(180deg,#f0d2c3,#d9b39f)}
.card-services .card-title{position:absolute;left:32px;top:50px}
.card-services .card-text{position:absolute;left:32px;top:116px;width:430px}
.card-services .btn{position:absolute;left:30px;top:215px;width:186px;height:48px}

.card-doctors{left:616px;top:1023px;width:505px;height:314px;
  background:linear-gradient(135deg,#5a4b44,#2c2826 60%,#4a413b)}
.card-doctors .card-title{position:absolute;left:24px;top:188px;font-size:52px}
.play-icon{position:absolute;left:196px;top:70px}

/* about */
.section-title{font-family:"Crimson Pro",serif;font-weight:700;color:var(--orange);font-size:58px}
.about-title{left:0;width:1200px;top:1440px;text-align:center}
.about-text{left:150px;width:900px;top:1526px;text-align:center;font-size:14.5px;line-height:1.45;color:var(--grey-light)}
.about-text p+p{margin-top:14px}
.about-btn{left:506px;top:1687px;width:186px;height:48px}

/* newsletter */
.news-title{left:78px;top:1992px}
.news-text{left:78px;top:2074px;width:520px;font-size:14.5px;line-height:1.45;color:var(--grey)}
.field{left:78px;width:450px;height:49px;border-radius:25px;background:var(--field);border:1px solid #d8d8d8;
  padding-left:26px;display:flex;align-items:center;font-size:14.5px;color:#888}
.news-btn{left:78px;top:2313px;width:188px;height:49px}
.consult-photo{left:528px;top:2074px;width:672px;height:420px;
  background:linear-gradient(90deg,rgba(255,255,255,0),#e8dcd2 25%,#d9c2b2 55%,#ece6e2)}

/* footer */
.footer-wave{left:0;top:2430px;width:1200px;height:506px}
.footer-col{top:2567px;color:var(--white);font-size:14.5px}
.footer-col h3{font-family:"Crimson Pro",serif;font-weight:700;font-size:24px;margin-bottom:16px}
.link-list{list-style:none;line-height:29.5px;color:#ffe6d4}
.link-list li:first-child{color:var(--white)}
.loc{padding-left:30px;position:relative}
.loc h4{font-family:"Crimson Pro",serif;font-weight:700;font-size:17px;margin-bottom:10px}
.loc p{color:#ffe6d4;line-height:1.4;margin-bottom:18px}
.loc svg{position:absolute;left:0}
.footer-brand{display:flex;align-items:center;gap:10px;font-weight:600;font-size:29px;color:var(--white);margin-bottom:18px}
.footer-brand .brand-dot{border-color:var(--white)}
.footer-about{color:#ffe6d4;line-height:1.45;width:240px}
.footer-rule{left:78px;top:2867px;width:1044px;height:1px;background:rgba(255,255,255,.6)}
.copyright{left:0;width:1200px;top:2891px;text-align:center;font-size:14px;color:#ffe6d4}
.copyright strong{color:var(--white)}
.copyright span{margin:0 12px}
</style>
</head>
<body>

<header class="site-header abs">
  <div class="brand abs"><span class="brand-dot"></span>Pelmora Hearing</div>
  <div class="header-tools abs">
    <svg width="28" height="32" viewBox="0 0 28 32" fill="none" stroke="#555" stroke-width="2"><circle cx="14" cy="10" r="7"/><path d="M2 31c0-7 5-12 12-12s12 5 12 12z"/></svg>
    <span class="divider"></span>
    <span class="phone-link">
      <svg width="24" height="24" viewBox="0 0 24 24"><circle cx="12" cy="12" r="11" fill="none" stroke="#f26a1b" stroke-width="2"/><path d="M8 6l2 0 1 3-1.5 1c.8 1.8 2 3 3.5 3.5l1-1.5 3 1 0 2c0 1-1 1.5-2 1.5C10 16 7 12 6.5 8 6.5 7 7 6 8 6z" fill="#f26a1b"/></svg>
      (02) 5550 1842
    </span>
  </div>
  <nav class="main-nav abs">
    <span>About Us</span><span>Your Hearing</span><span>Hearing Aids</span><span>Musicians</span><span>Doctors Information</span><span>Products</span><span>Contact Us</span>
  </nav>
</header>

<div class="hero-product abs" role="img" aria-label="Photo of a behind-the-ear hearing aid with its receiver"></div>
<h1 class="hero-title abs">AUDIOLOGIST</h1>
<p class="hero-sub abs">Will help you hear the sounds that you have been missing for so long.</p>
<a class="btn hero-btn abs">LEARN MORE</a>

<section class="card card-aids abs">
  <h2 class="card-title">Hearing Aids</h2>
  <p class="card-text">When considering a hearing aid it is important that you understand your hearing loss and your expectations of a hearing aid. There may be several hearing aids that are appropriate to your hearing loss, but there may only be one or two that comfortably fit the shape of your ear and successfully fit in with your life style. Many good hearing aids have automatic features such as a directional microphones and volume control.</p>
  <a class="btn">LEARN MORE</a>
  <div class="aids-photo" role="img" aria-label="Photo of a row of hearing aids in various colours"></div>
</section>

<section class="card card-services abs">
  <div class="services-photo" role="img" aria-label="Photo of a woman cupping her ear to listen"></div>
  <h2 class="card-title">Services</h2>
  <p class="card-text">Each of our custom built clinics have the most up to date diagnostic equipment available. We offer an extensive range of diagnostics conducted by highly experienced and fully trained Audiologists.</p>
  <a class="btn">LEARN MORE</a>
</section>

<section class="card card-doctors abs" role="img" aria-label="Video still of an audiologist examining a patient">
  <svg class="play-icon" width="108" height="108" viewBox="0 0 108 108"><circle cx="54" cy="54" r="49" fill="none" stroke="#f26a1b" stroke-width="7"/><path d="M42 32l34 22-34 22z" fill="#f26a1b"/></svg>
  <h2 class="card-title">Doctors Information</h2>
</section>

<h2 class="section-title about-title abs">About Us</h2>
<div class="about-text abs">
  <p>Pelmora Hearing is an independently owned and managed professional audiology clinic. Our Audiologists are health-care professionals specialising in diagnosing, treating and monitoring everything to do with hearing and balance. At Pelmora Hearing we work closely with Ear, Nose and Throat specialists to ensure you receive the highest standards of medical care.</p>
  <p>Pelmora Hearing are state of the art hearing and balance clinics. We provide all brands of digital hearing aids, cochlear implants and assisted listening devices. We are diagnostic clinics, offering hearing tests for adults and children, balance tests, tinnitus testing and treatment, and auditory processing tests (APD).</p>
</div>
<a class="btn about-btn abs">LEARN MORE</a>

<div class="consult-photo abs" role="img" aria-label="Photo of a doctor checking an elderly man's ear with an otoscope"></div>
<h2 class="section-title news-title abs">Newsletter</h2>
<p class="news-text abs">Keep up with the latest trends and advances in hearing health. Sign up for our quarterly newsletter.</p>
<div class="field abs" style="top:2139px">Name</div>
<div class="field abs" style="top:2197px">Phone</div>
<div class="field abs" style="top:2256px">Email</div>
<a class="btn news-btn abs">VIEW ALL</a>

<svg class="footer-wave abs" viewBox="0 0 1200 506" preserveAspectRatio="none">
  <defs>
    <linearGradient id="foot" x1="0" y1="0" x2="0" y2="1"><stop offset="0" stop-color="#ff9a1f"/><stop offset=".25" stop-color="#f57420"/><stop offset="1" stop-color="#f0610f"/></linearGradient>
  </defs>
  <path d="M0 60 C300 20 700 20 1200 30 L1200 506 L0 506Z" fill="#ffc24a"/>
  <path d="M0 85 C350 40 800 55 1200 50 L1200 506 L0 506Z" fill="url(#foot)"/>
</svg>

<div class="footer-col abs" style="left:78px">
  <h3>Usefull Links</h3>
  <ul class="link-list"><li>Home</li><li>About Us</li><li>Your Hearing</li><li>Hearing Aids</li><li>Musicians</li><li>Doctors Information</li><li>Products</li><li>Contact Us</li></ul>
</div>
<div class="footer-col abs" style="left:344px;width:240px">
  <h3>Harbourview</h3>
  <div class="loc"><h4>Address :</h4><p>Ground Floor, Suite 3,<br>18 Wattle Parade, Harbourview,<br>NSW, 2071</p><h4>Phone :</h4><p>5550 1842</p></div>
</div>
<div class="footer-col abs" style="left:609px;width:260px">
  <h3>Elm Grove</h3>
  <div class="loc">
    <svg style="top:0" width="16" height="22" viewBox="0 0 16 22"><path d="M8 0a8 8 0 0 0-8 8c0 6 8 14 8 14s8-8 8-14a8 8 0 0 0-8-8z" fill="#fff"/><circle cx="8" cy="8" r="3" fill="#f26a1b"/></svg>
    <h4>Address :</h4><p>Shop 7,<br>42 Carrington Road Elm Grove,<br>NSW, 2093</p>
    <svg style="top:104px" width="18" height="18" viewBox="0 0 24 24"><path d="M6 2h4l2 5-2.5 1.5c1.2 2.6 3.2 4.6 6 6L17 12l5 2v4c0 2-2 3-4 3C10 20 4 14 3 6c0-2 1-4 3-4z" fill="#fff"/></svg>
    <h4>Phone :</h4><p>5550 3967</p>
  </div>
</div>
<div class="footer-col abs" style="left:875px">
  <div class="footer-brand"><span class="brand-dot"></span>Pelmora Hearing</div>
  <p class="footer-about">Pelmora Hearing is an independently owned and managed professional audiology clinic. Our Audiologists are health-care professionals specialising in diagnosing, treating and monitoring everything to do with hearing and balance.</p>
</div>

<div class="footer-rule abs"></div>
<p class="copyright abs">© <strong>Pelmora Hearing</strong> - 2018. All rights reserved.<span>|</span>Shipping, Return &amp; Refund Policy<span>|</span>Terms &amp; Conditions</p>

</body>
</html>
```